BRTW Traditional Business Card Project

Please see attached....just a simple business card... on attachment- please use the exact font, style, etc as the attached "Dal Rupert Huxley" card... however, replace with the "Owen Bartholomew Lindqvist" text and address below the card.

```html
<!DOCTYPE html>
<html lang="en">
<head>
<meta charset="utf-8">
<title>BRTW Business Card – Owen Bartholomew Lindqvist</title>
<link href="https://fonts.googleapis.com/css2?family=Tinos&family=Arimo&display=swap" rel="stylesheet">
<style>
  :root {
    --backdrop: #7a7a7a;
    --card: #eef0ef;
    --ink: #141618;
  }
  html, body {
    margin: 0;
    width: 1200px;
    height: 1200px;
    overflow: hidden;
    background: var(--backdrop);
  }
  .card {
    position: absolute;
    left: 75px;
    top: 300px;
    width: 1050px;
    height: 600px;
    background: var(--card);
    color: var(--ink);
    box-shadow: 0 6px 18px rgba(0,0,0,0.35);
  }
  .firm {
    position: absolute;
    left: 78px;
    top: 58px;
  }
  .firm-name {
    font-family: "Tinos", "Times New Roman", serif;
    font-variant: small-caps;
    font-size: 48px;
    letter-spacing: 1px;
    line-height: 1;
  }
  .firm-sub {
    font-family: "Arimo", Arial, sans-serif;
    font-size: 21px;
    letter-spacing: 4px;
    margin: 4px 0 0 52px;
  }
  .person {
    position: absolute;
    left: 140px;
    top: 232px;
  }
  .person-name {
    font-family: "Tinos", "Times New Roman", serif;
    font-variant: small-caps;
    font-size: 66px;
    line-height: 1;
  }
  .person-title {
    font-family: "Arimo", Arial, sans-serif;
    font-size: 22px;
    letter-spacing: 5px;
    margin: 2px 0 0 190px;
  }
  .address, .contact {
    position: absolute;
    font-family: "Arimo", Arial, sans-serif;
    font-size: 20px;
    line-height: 1.3;
    letter-spacing: 2px;
  }
  .address { left: 78px; top: 425px; }
  .contact { right: 78px; top: 470px; }
  .lower { letter-spacing: 0.5px; }
</style>
</head>
<body>
  <div class="card">
    <div class="firm">
      <div class="firm-name">Bay Ridge Trial Works</div>
      <div class="firm-sub">GROUP, PLC</div>
    </div>
    <div class="person">
      <div class="person-name">Owen Bartholomew Lindqvist</div>
      <div class="person-title">ATTORNEY AT LAW</div>
    </div>
    <div class="address">
      2417 CEDAR LANE, SUITE B<br>
      MAPLE GROVE, CA 91488<br>
      <span class="lower">www.brtwlaw.com</span>
    </div>
    <div class="contact">
      TEL (555) 312-4400<br>
      FAX (555) 312-4401<br>
      <span class="lower">olindqvist@brtwlaw.com</span>
    </div>
  </div>
</body>
</html>
```